Established Mortgage Brokerage Needs Wordpress Site for Corporate website

We need a wordpress website designed for a well-established Mortgage Brokerage in Oakville, Ontario. Our firm provides residential and commercial mortgage solutions for clients in Ontario, Canada. The final design should communicate professionalism, reliability, trustworthiness, financial stability. Colour scheme should be in line with our logo per attached files.

Target Market(s)

End consumer is knowledgable. Will vary from working families to business professionals, looking for financing alternatives for various types of real estate.

Other font styles liked:
• Please keep in line with Logo

Colors
3277b5

Requirements
Must have
• Site will have 10 pages. Logo must be included.
• Navigation menue will consist of Home, About, Services (with 3 pages in drop down Services offered, Mortgage FAQ and Realotrs), Calculators, Apply Now , Blog and Contact.
• Font should be in line with logo.
Nice to have
• Bright pictures, simplicity, and overall feeling of professionalism/knowledge.

```html
<!DOCTYPE html>
<html lang="en">
<head>
<meta charset="utf-8">
<title>Maplecrest Mortgage Group</title>
<link href="https://fonts.googleapis.com/css2?family=Oswald:wght@300;400;500&display=swap" rel="stylesheet">
<style>
  :root {
    --brand-blue: #55a9dc;
    --brand-blue-dark: #3f93c8;
    --charcoal: #3a3a3a;
    --dropdown-grey: #7d7d7d;
    --page-bg: #efefef;
    --white: #ffffff;
    --body-text: #8a8a8a;
    --footer-text: #333333;
    --button-grey: #e6e6e6;
    --label-black: #0d0d0d;
  }
  * { box-sizing: border-box; margin: 0; padding: 0; }
  html, body {
    width: 1200px; height: 2500px; overflow: hidden;
  }
  body {
    position: relative;
    background: radial-gradient(ellipse at top, #f8f8f8 0%, var(--page-bg) 55%, #e4e4e4 100%);
    font-family: "Oswald", "Arial Narrow", sans-serif;
    font-weight: 300;
  }

  /* Brand mark */
  .brand {
    position: absolute; top: 32px; left: 0; width: 1200px;
    text-align: center; color: var(--brand-blue); font-weight: 500;
  }
  .brand-dot {
    width: 62px; height: 62px; border-radius: 50%;
    background: var(--brand-blue); margin: 0 auto 6px;
  }
  .brand-name { font-size: 30px; line-height: 32px; letter-spacing: 1px; }
  .brand-tag { font-size: 12px; line-height: 14px; letter-spacing: 1px; }

  .site { position: absolute; left: 132px; width: 936px; }

  /* Navigation */
  .main-nav {
    top: 185px; height: 82px; background: var(--brand-blue);
    display: flex; align-items: center; justify-content: space-between;
    padding: 0 30px 0 32px;
  }
  .main-nav a {
    color: var(--white); text-decoration: none; font-size: 26px;
    font-weight: 400; text-transform: uppercase;
  }
  .dropdown {
    position: absolute; top: 267px; left: 378px; width: 210px; height: 116px;
    background: var(--dropdown-grey); padding: 18px 0 0 26px; z-index: 3;
  }
  .dropdown a {
    display: block; color: var(--white); text-decoration: none;
    font-size: 15px; font-weight: 400; line-height: 38px;
  }

  /* Hero */
  .hero { top: 267px; height: 483px; overflow: hidden; }
  .hero-photo {
    position: absolute; inset: 0;
    background: linear-gradient(160deg, #2d3a2a 0%, #4a3a28 35%, #8a5a32 60%, #c98a4a 80%, #e4c38a 100%);
  }
  .hero-title {
    position: absolute; top: 205px; left: 0; width: 936px; text-align: center;
    color: var(--white); text-transform: uppercase;
  }
  .hero-title h1 { font-size: 68px; font-weight: 400; line-height: 72px; }
  .hero-title p { font-size: 31px; font-weight: 300; line-height: 36px; }
  .hero-badge {
    position: absolute; left: 35px; top: 383px; color: var(--white);
    font-size: 15px; font-weight: 500;
  }
  .slider-dots {
    position: absolute; right: 20px; top: 382px;
    display: flex; flex-direction: column; gap: 10px;
  }
  .slider-dots span { width: 10px; height: 10px; border-radius: 50%; background: var(--white); }
  .slider-dots span.active { background: var(--brand-blue); }

  /* Welcome */
  .welcome {
    top: 750px; height: 363px; background: var(--charcoal);
    text-align: center; color: var(--white); padding: 48px 0 0;
  }
  .welcome h2 { font-size: 42px; font-weight: 400; text-transform: uppercase; line-height: 50px; }
  .welcome p {
    width: 800px; margin: 26px auto 0; font-size: 13.5px; line-height: 27px; color: #e6e6e6;
  }
  .btn-primary {
    display: inline-block; margin-top: 28px; width: 205px; height: 50px; line-height: 50px;
    background: var(--brand-blue); color: var(--white); font-size: 24px; font-weight: 400;
    text-decoration: none; text-transform: uppercase;
  }

  /* Services */
  .services { top: 1113px; height: 694px; background: var(--white); }
  .section-title {
    position: absolute; top: 50px; left: 0; width: 936px; text-align: center;
    color: var(--brand-blue); font-size: 42px; font-weight: 400; text-transform: uppercase;
  }
  .service-card { position: absolute; top: 140px; width: 442px; }
  .service-card.faq { left: 13px; }
  .service-card.realtors { left: 481px; }
  .service-photo { position: relative; height: 314px; }
  .faq .service-photo { background: linear-gradient(180deg, #2f7fc4 0%, #7fbde6 45%, #d9e2e4 65%, #4f8a3f 85%, #2aa7c9 100%); }
  .realtors .service-photo { background: linear-gradient(180deg, #9a8a7a 0%, #c4b8aa 40%, #7a8aa0 70%, #5c7a3c 100%); }
  .service-label {
    position: absolute; left: 0; bottom: 27px; width: 192px; height: 57px;
    background: var(--label-black); color: var(--brand-blue);
    font-size: 25px; font-weight: 400; line-height: 57px; padding-left: 23px;
    text-transform: uppercase;
  }
  .service-card p {
    margin-top: 33px; font-size: 13.5px; line-height: 26px; color: var(--body-text);
  }
  .btn-read {
    display: inline-block; margin-top: 30px; width: 116px; height: 35px; line-height: 35px;
    background: var(--button-grey); color: #888; font-size: 13px; text-align: center;
    text-decoration: none;
  }

  /* Testimonials */
  .testimonials { top: 1807px; height: 466px; background: var(--brand-blue); color: var(--white); text-align: center; }
  .testimonials h2 {
    position: absolute; top: 45px; left: 0; width: 936px; font-size: 42px; font-weight: 400;
    text-transform: uppercase;
  }
  .quote-mark { position: absolute; top: 143px; left: 448px; }
  .rule { position: absolute; left: 163px; width: 610px; height: 1px; background: rgba(255,255,255,.85); }
  .rule.top { top: 230px; }
  .rule.bottom { top: 385px; }
  .testimonials blockquote {
    position: absolute; top: 265px; left: 40px; width: 856px;
    font-size: 13.5px; line-height: 27px; color: #f2f7fb;
  }
  .testimonials cite {
    position: absolute; top: 417px; left: 0; width: 936px; display: block;
    text-align: center; font-style: normal;
    font-size: 20px; font-weight: 400; text-transform: uppercase;
  }

  /* Footer */
  .social {
    position: absolute; top: 2332px; left: 0; width: 1200px;
    display: flex; justify-content: center; gap: 28px;
  }
  .social span { width: 22px; height: 22px; border-radius: 50%; background: var(--brand-blue); }
  .footer-nav {
    position: absolute; top: 2382px; left: 0; width: 1200px; text-align: center;
    font-size: 15px; font-weight: 400; color: var(--footer-text); text-transform: uppercase;
  }
  .footer-nav a { color: var(--footer-text); text-decoration: none; padding: 0 14px; }
  .footer-nav .sep { color: #555; }
  .copyright {
    position: absolute; top: 2437px; left: 0; width: 1200px; text-align: center;
    font-size: 14px; font-weight: 400; color: var(--footer-text); text-transform: uppercase;
  }
</style>
</head>
<body>

  <header class="brand">
    <div class="brand-dot"></div>
    <div class="brand-name">MAPLECREST</div>
    <div class="brand-tag">MORTGAGE GROUP</div>
  </header>

  <nav class="site main-nav">
    <a href="#">Home</a>
    <a href="#">About</a>
    <a href="#">Services</a>
    <a href="#">Calculators</a>
    <a href="#">Apply Now</a>
    <a href="#">Blog</a>
    <a href="#">Contact</a>
  </nav>
  <div class="dropdown">
    <a href="#">MORTGAGE FAQ</a>
    <a href="#">REALTORS</a>
  </div>

  <section class="site hero">
    <div class="hero-photo" role="img" aria-label="Modern home with a lit wooden deck and patio lounge furniture at dusk"></div>
    <div class="hero-title">
      <h1>Maplecrest</h1>
      <p>Moratage Group</p>
    </div>
    <div class="hero-badge">MAPLECREST</div>
    <div class="slider-dots"><span class="active"></span><span></span><span></span><span></span></div>
  </section>

  <section class="site welcome">
    <h2>Welcome to Moratage Maplecrest</h2>
    <p>At vero eos et accusamus et iusto odio dignissimos ducimus qui blanditiis praesentium voluptatum deleniti atque corrupti quos dolores et quas molestias excepturi sint occaecati cupiditate non provident, similique sunt in culpa qui officia deserunt mollitia animi, id est laborum et dolorum fuga. Et harum quidem rerum facilis est et expedita distinctio. Nam libero tempore, cum soluta nobis est eligendi optio cumque nihil impedit quo minus id quod maxime placeat facere possimus, omnis voluptas assumenda est, omnis dolor repellendus.</p>
    <a class="btn-primary" href="#">Contact Us</a>
  </section>

  <section class="site services">
    <h2 class="section-title">Services</h2>
    <article class="service-card faq">
      <div class="service-photo" role="img" aria-label="White modern villa with palm trees and a swimming pool under blue sky">
        <div class="service-label">Mortgage FAQ</div>
      </div>
      <p>At vero eos et accusamus et iusto odio dignissimos ducimus qui blanditiis praesentium voluptatum deleniti atque corrupti quos dolores et quas molestias excepturi sint occaecati cupiditate non provident, similique sunt in culpa qui officia</p>
      <a class="btn-read" href="#">Read More</a>
    </article>
    <article class="service-card realtors">
      <div class="service-photo" role="img" aria-label="Couple shaking hands with a realtor in front of a brick house with a sold sign">
        <div class="service-label">Realtors</div>
      </div>
      <p>At vero eos et accusamus et iusto odio dignissimos ducimus qui blanditiis praesentium voluptatum deleniti atque corrupti quos dolores et quas molestias excepturi sint occaecati cupiditate non provident, similique sunt</p>
      <a class="btn-read" href="#">Read More</a>
    </article>
  </section>

  <section class="site testimonials">
    <h2>Testimonials</h2>
    <svg class="quote-mark" width="40" height="34" viewBox="0 0 40 34" aria-hidden="true">
      <path d="M2 34 V18 C2 8 6 2 15 0 L16 5 C10 7 8 11 8 16 H16 V34 Z M23 34 V18 C23 8 27 2 36 0 L37 5 C31 7 29 11 29 16 H37 V34 Z" fill="#ffffff"/>
    </svg>
    <div class="rule top"></div>
    <blockquote>At vero eos et accusamus et iusto odio dignissimos ducimus qui blanditiis praesentium voluptatum deleniti atque corrupti quos dolores et quas molestias excepturi sint occaecati cupiditate non provident, similique sunt in culpa qui officia deserunt mollitia animi, id est laborum et dolorum fuga. Et harum quidem rerum facilis est et expedita distinctio. Nam libero tempore, cum soluta nobis est eligendi optio</blockquote>
    <div class="rule bottom"></div>
    <cite>Daniel Rourke</cite>
  </section>

  <footer>
    <div class="social" aria-label="Social links"><span></span><span></span><span></span><span></span><span></span></div>
    <nav class="footer-nav">
      <a href="#">Home</a><span class="sep">|</span><a href="#">About</a><span class="sep">|</span><a href="#">Services</a><span class="sep">|</span><a href="#">Calculators</a><span class="sep">|</span><a href="#">Apply Now</a><span class="sep">|</span><a href="#">Blog</a><span class="sep">|</span><a href="#">Contact</a>
    </nav>
    <div class="copyright">&copy; 2016 Company Name &nbsp;|&nbsp;All Rights Reserved</div>
  </footer>

</body>
</html>
```